MailChimp newsletter template & Facebook / LinkedIn header design for VORANEL group

Hi all,
We are VORANEL: a company providing technology solutions to the construction industry. We have a brand new website - www.voranelworks.com - and are looking for a MailChimp Newsletter Template that matches our new website design. In addition, we are looking for a Facebook and LinkedIn header in line with our new website and news letter template.
Our company is located in 4 countries. Please visit our website for more information about our company:
The Netherlands - www.voranelworks.nl
Denmark - www.voranelworks.dk
Sweden - www.voranelworks.se
Norway - www.voranelworks.no
An English translation can be accessed via www.voranelworks.com.
Look and Feel:
In line with our website (please refer to links above)
Match the high-tech, innovative, fresh character of our company VORANEL
Keywords: clean / simple / robust

Updates
Project Deadline Extended
Reason: Due to the holidayweekend, we weren't able to provide all designers sufficient and equal feedback. Therefore we have delayed the deadline with three days.

Target Market(s)
Building / construction companies in Northern Europe.
Industry/Entity Type
Construction
Colors
Designer to choose colors to be used in the design.
Requirements
Must have
- Requirements for News letter template:
Use of our VORANEL logo (attached)
Use of VORANEL grid in line with our website (attached)
Use of the VORANEL colours
Links to Social Media
Room for promotions
Room for upcoming events
Promotion of our new website www.voranelworks.com
To be used for email and PDF
Requirements for Facebook / LinkedIn:
Use of the VORANEL colours
Should not have
- A lot of small details. complicated design.

```html
<!DOCTYPE html>
<html lang="en">
<head>
<meta charset="utf-8">
<title>VORANEL Newsletter</title>
<link href="https://fonts.googleapis.com/css2?family=Source+Sans+3:ital,wght@0,400;0,600;0,700;1,400&display=swap" rel="stylesheet">
<style>
:root{
  --navy:#0b4379;
  --navy-deep:#083663;
  --orange:#ec9b32;
  --yellow:#f6c55a;
  --grey-bg:#f2f2f2;
  --grey-date:#c9c9c9;
  --text:#3c3c3c;
  --muted:#6e6e6e;
  --dark:#2e2e2e;
  --white:#ffffff;
}
*{margin:0;padding:0;box-sizing:border-box}
html,body{width:1200px;height:2492px;overflow:hidden;background:var(--white)}
body{font-family:"Source Sans 3",Arial,sans-serif;color:var(--text);position:relative}
.abs{position:absolute}

/* header */
.header{top:0;left:0;width:1200px;height:182px;background:var(--white)}
.brand{left:24px;top:44px;display:flex;align-items:center;gap:14px}
.brand-mark{width:26px;height:26px;background:var(--orange)}
.brand-name{font-size:76px;font-weight:700;color:var(--navy);letter-spacing:1px;line-height:1}
.flags{right:30px;top:88px;display:flex;gap:58px}
.flags svg{width:34px;height:24px;display:block}

.tagline{top:182px;left:0;width:1200px;height:92px;background:var(--navy);color:var(--white);
  font-size:38px;text-align:center;line-height:92px;letter-spacing:.5px}

/* hero */
.hero{top:274px;left:0;width:1200px;height:374px;
  background:linear-gradient(110deg,#b9853a 0%,#d9a24a 35%,#c88d3c 60%,#a56f2c 100%)}
.hero-strip{top:648px;left:0;width:1200px;height:8px;background:var(--navy)}
.promo-line{left:16px;background:rgba(255,255,255,.92);color:#555;font-size:44px;
  height:58px;line-height:58px;padding:0 18px}
.promo-1{top:386px;width:474px}
.promo-2{top:450px;width:722px}
.promo-cta{left:16px;top:520px;width:246px;height:58px;background:var(--yellow);
  color:#6b5a32;font-size:38px;line-height:58px;padding-left:18px}

/* product tiles */
.tile{width:356px;height:248px;color:var(--white);font-size:27px;display:flex;
  align-items:flex-end;justify-content:center;padding-bottom:10px;letter-spacing:.3px}
.tile-warm{background:linear-gradient(160deg,#e4b468,#b7843b 60%,#8b5f2a)}
.tile-soft{background:linear-gradient(180deg,#f2f2f2,#d8d8d8 60%,#b4b4b4)}
.tile-field{background:linear-gradient(180deg,#8db4d8 0%,#a9c4d4 40%,#5d8a3a 60%,#3f6a2a 100%)}
.tile-screen{background:linear-gradient(150deg,#8d6a3e,#c79a58 50%,#6d4c26)}

.cta-band{top:1266px;left:0;width:1200px;height:88px;background:var(--orange);color:var(--white);
  font-size:38px;text-align:center;line-height:88px}

/* events */
.events{top:1354px;left:0;width:1200px;height:352px;background:var(--grey-bg)}
.date{width:136px}
.date-month{height:76px;background:var(--navy);color:var(--white);font-size:38px;text-align:center;line-height:76px}
.date-day{height:80px;background:var(--grey-date);color:var(--white);font-size:44px;text-align:center;line-height:80px}
.event-text{width:340px}
.event-title{color:var(--navy);font-weight:700;font-size:28px;line-height:32px}
.event-body{margin-top:10px;font-size:23px;line-height:29px;color:var(--text)}

/* testimonial */
.quote-mark{top:1736px;left:0;width:1200px;text-align:center;font-size:130px;color:#8b8b8b;font-weight:700;line-height:1}
.quote{top:1856px;left:40px;width:1120px;text-align:center;font-style:italic;font-size:29px;line-height:40px;color:var(--muted)}
.quote-by{top:2032px;left:0;width:1200px;text-align:center;font-size:29px;font-weight:600;color:var(--text)}

/* footer */
.offices{top:2148px;left:0;width:1200px;height:268px;
  background:radial-gradient(ellipse at 55% 30%,#2a64a0 0%,#164f8a 45%,#0b3f74 100%)}
.office{width:260px;text-align:center;color:var(--white);font-size:26px}
.office-name{line-height:34px}
.office-phone{margin-top:52px}
.social{top:2416px;left:0;width:1200px;height:76px;background:var(--dark);display:flex;justify-content:center;align-items:center;gap:34px}
.social span{width:42px;height:42px;display:block}
.s1{background:#3c78c8}.s2{background:#5aa0d8}.s3{background:#c9503e}
</style>
</head>
<body>

<header class="abs header">
  <div class="abs brand"><span class="brand-mark"></span><span class="brand-name">VORANEL</span></div>
  <div class="abs flags">
    <svg viewBox="0 0 34 24" role="img" aria-label="Danish flag"><rect width="34" height="24" fill="#d0262f"/><rect x="10" width="4" height="24" fill="#fff"/><rect y="10" width="34" height="4" fill="#fff"/></svg>
    <svg viewBox="0 0 34 24" role="img" aria-label="Dutch flag"><rect width="34" height="8" fill="#c3283a"/><rect y="8" width="34" height="8" fill="#fff"/><rect y="16" width="34" height="8" fill="#2a4c94"/></svg>
    <svg viewBox="0 0 34 24" role="img" aria-label="Norwegian flag"><rect width="34" height="24" fill="#c8283a"/><rect x="9" width="6" height="24" fill="#fff"/><rect y="9" width="34" height="6" fill="#fff"/><rect x="10.5" width="3" height="24" fill="#1f3f86"/><rect y="10.5" width="34" height="3" fill="#1f3f86"/></svg>
    <svg viewBox="0 0 34 24" role="img" aria-label="Swedish flag"><rect width="34" height="24" fill="#1f65a8"/><rect x="10" width="4" height="24" fill="#f4c91c"/><rect y="10" width="34" height="4" fill="#f4c91c"/></svg>
  </div>
</header>

<div class="abs tagline">YOUR CONSTRUCTION TECHNOLOGY PROVIDER</div>

<div class="abs hero" role="img" aria-label="Construction site with bulldozers and a surveyor, warm golden tone"></div>
<div class="abs hero-strip"></div>
<div class="abs promo-line promo-1">GET 20% OFF ON ALL</div>
<div class="abs promo-line promo-2">LASERS AND SCANNING PRODUCTS</div>
<div class="abs promo-cta">Learn More</div>

<div class="abs tile tile-warm" style="left:24px;top:690px" role="img" aria-label="Excavator on a site">GRADE CONTROL SYSTEM</div>
<div class="abs tile tile-warm" style="left:422px;top:690px" role="img" aria-label="Surveyor beside a dozer">SITE POSITIONING SYSTEM</div>
<div class="abs tile tile-warm" style="left:824px;top:690px" role="img" aria-label="Loader bucket full of earth">WEIGHING SYSTEM</div>
<div class="abs tile tile-screen" style="left:24px;top:976px" role="img" aria-label="Field tablet showing software">SOFTWARE</div>
<div class="abs tile tile-soft" style="left:422px;top:976px" role="img" aria-label="Laser levels and receivers">LASERS</div>
<div class="abs tile tile-field" style="left:824px;top:976px" role="img" aria-label="Tractors with machine control">MCS PRODUCTS</div>

<div class="abs cta-band">VIEW ALL PRODUCTS</div>

<section class="abs events"></section>
<div class="abs date" style="left:20px;top:1432px"><div class="date-month">JAN</div><div class="date-day">14</div></div>
<div class="abs event-text" style="left:180px;top:1430px">
  <div class="event-title">LOREM IPSUM DOLOR SIT</div>
  <div class="event-body">Lorem ipsum dolor sit amet, consectetuer adipiscing elit, sed diam nonummy nibh euismod tincidunt ut laoreet dolore.</div>
</div>
<div class="abs date" style="left:602px;top:1432px"><div class="date-month">JAN</div><div class="date-day">14</div></div>
<div class="abs event-text" style="left:764px;top:1430px">
  <div class="event-title">LOREM IPSUM DOLOR SIT</div>
  <div class="event-body">Lorem ipsum dolor sit amet, consectetuer adipiscing elit, sed diam nonummy nibh euismod tincidunt ut laoreet dolore.</div>
</div>

<div class="abs quote-mark">&ldquo;</div>
<p class="abs quote">The machine is very user friendly. As a result of VORANEL’s great service and support, I was able to learn how to measure stake with GPS in just a couple of weeks. Therefore, I could use the Essential Kit was on the job site right away!”</p>
<p class="abs quote-by">-Company Brevik about the TRX Essential Kit</p>

<footer class="abs offices" role="img" aria-label="Faint world map background"></footer>
<div class="abs office" style="left:52px;top:2192px"><div class="office-name">VORANEL<br>NETHERLANDS</div><div class="office-phone">+31 (0) 55 2047300</div></div>
<div class="abs office" style="left:328px;top:2192px"><div class="office-name">VORANEL<br>DENMARK</div><div class="office-phone">+45 70 61 38 20</div></div>
<div class="abs office" style="left:618px;top:2192px"><div class="office-name">VORANEL<br>SWEDEN</div><div class="office-phone">+46 (0) 10 7391500</div></div>
<div class="abs office" style="left:922px;top:2192px"><div class="office-name">VORANEL<br>NORWAY</div><div class="office-phone">+47 32 40 17 65</div></div>

<nav class="abs social" aria-label="Social media links">
  <span class="s1" role="img" aria-label="Social link 1"></span>
  <span class="s2" role="img" aria-label="Social link 2"></span>
  <span class="s3" role="img" aria-label="Social link 3"></span>
</nav>

</body>
</html>
```